Website for Prestigious Trailers and Floats

Design a prestigious website, to be used on mobile phones, and computers.
Must be able to be edited by myself
Please refer to www.marrowbeckhaulage.com.au
Needs to focus on the "Marrowbeck Trailers"" name, and the "Dunmere Ashby Trailers" name.
Three trailer types to be highlighted are QX408/QX412 Horse Floats, RV3072 /RV81 Trailers, and LP5840/5296 Tipper Trailers
Needs Home Page,
Home page to include highlighted trailer types, slider for testimonials, Phone number, location, social media links, blog/news spot
Page for each of the highlighted trailer types/variations on the model
Page for multiple other trailer types

Logo's attached, can be broken up and used in parts if necessary for design

Target Market(s)

Western Australia, Horse People, Commercial Trailer Users, Handymen, Mini Digger Users, Tradesmen

Industry/Entity Type

Mining, Commercial, Government, Trades, Industry, Hobbyist

Coding

Coded - Design and coding required

Number of Pages Required

5+ page

Requirements
Must have
• See brief above
Nice to have
• See brief above

```html
<!DOCTYPE html>
<html lang="en">
<head>
<meta charset="utf-8">
<title>Marrowbeck Trailers – Heavy Duty Trailers &amp; General Fabrication</title>
<link rel="stylesheet" href="https://fonts.googleapis.com/css2?family=Montserrat:wght@400;500;600;700&family=Uncial+Antiqua&display=swap">
<style>
:root{
  --orange:#d2462a;
  --orange-soft:#e0603a;
  --ink:#111;
  --dark:#1c1411;
  --dark-2:#2a1b15;
  --white:#fff;
  --text:#333;
}
*{box-sizing:border-box;margin:0;padding:0}
html,body{width:1200px;height:3667px;overflow:hidden}
body{position:relative;background:var(--white);font-family:"Montserrat",sans-serif;color:var(--text)}
.abs{position:absolute}
.display{font-family:"Uncial Antiqua",serif;color:var(--orange);text-transform:uppercase;letter-spacing:2px;font-weight:400}

.hero{left:0;top:0;width:1200px;height:730px;background:var(--dark-2)}
.hero-photo{left:0;top:0;width:1200px;height:575px;background:linear-gradient(180deg,#2b3440 0%,#55614e 35%,#3f5a2c 60%,#2d3a22 100%)}
.hero-shade{left:0;top:0;width:1200px;height:575px;background:linear-gradient(90deg,rgba(0,0,0,.55) 0%,rgba(0,0,0,.15) 55%,rgba(0,0,0,0) 100%)}
.trailer-photo{left:630px;top:150px;width:440px;height:390px;border-radius:30px 30px 10px 10px;background:linear-gradient(180deg,#d9d6cf,#a8a49a)}
.call{left:150px;top:30px;color:var(--orange-soft);font-size:15px;font-weight:600}
.phone{left:150px;top:48px;color:var(--white);font-size:21px;font-weight:700;letter-spacing:.5px}
.brand{left:330px;top:22px;width:540px;height:52px;display:flex;align-items:center;justify-content:center;gap:12px}
.brand-mark{width:16px;height:16px;background:var(--orange)}
.brand-name{font-weight:700;font-size:26px;color:var(--orange-soft);letter-spacing:2px;text-transform:uppercase}
.socials{left:910px;top:36px;display:flex;gap:13px}
.socials span{width:36px;height:36px;border-radius:50%;display:block}
.nav{font-size:12px;color:var(--white);font-weight:500}
.nav a{color:var(--white);text-decoration:none;position:absolute;white-space:nowrap}
.nav a.active{color:var(--orange-soft);text-decoration:underline}
.hero-frame{left:168px;top:186px;width:95px;height:242px;border:5px solid var(--orange);border-right:none}
.hero-frame-line{left:168px;top:423px;width:270px;height:5px;background:var(--orange)}
.hero-title{left:209px;top:212px;width:385px;color:var(--white);font-size:30px;font-weight:700;line-height:39px}
.btn{display:flex;align-items:center;justify-content:center;font-size:12px;font-weight:500}
.btn-sales{left:420px;top:410px;width:78px;height:28px;background:var(--white);color:var(--ink);border-right:4px solid var(--orange);border-bottom:3px solid var(--orange)}
.covered{left:235px;top:620px;color:var(--white);font-size:19px;font-weight:600;line-height:25px}
.date{top:631px;width:131px;height:41px;border:1px solid #4a352c;background:#22170f;color:var(--white)}
.date svg{position:absolute;left:12px;top:12px}
.date .lbl{position:absolute;left:46px;top:5px;font-size:10px;color:var(--orange-soft)}
.date .val{position:absolute;left:46px;top:20px;font-size:11px}
.date-go{left:921px;top:631px;width:44px;height:41px;background:var(--orange)}

.partner{left:154px;top:833px;width:287px;height:192px;display:flex;align-items:center;gap:12px}
.partner-mark{width:22px;height:22px;background:#1a3a9c;flex:none}
.partner-name{font-size:27px;font-weight:700;color:#1a3a9c;line-height:32px}
.intro-title{left:507px;top:810px;width:480px;font-size:25px;line-height:30px}
.intro-sub{left:507px;top:921px;font-size:11px;font-weight:700;color:var(--ink)}
.intro-copy{left:507px;top:940px;width:460px;font-size:10.5px;line-height:15px}
.intro-copy p{margin-bottom:14px}

.band{left:0;width:1200px}
.section-title{width:1200px;left:0;text-align:center;font-size:27px}

.card{background:var(--white);width:251px}
.card-photo{position:absolute;left:7px;top:9px;width:237px;height:223px}
.card-name{position:absolute;left:0;width:100%;text-align:center;top:250px;font-size:16px;font-weight:600;color:var(--ink)}
.card-code{position:absolute;left:0;width:100%;text-align:center;top:272px;font-size:11px;color:var(--orange)}
.blog-photo{position:absolute;left:7px;top:8px;width:237px;height:178px}
.blog-date{position:absolute;left:18px;top:204px;font-size:10px;font-weight:600;color:var(--ink);display:flex;gap:6px;align-items:center}
.blog-text{position:absolute;left:18px;top:226px;width:215px;font-size:10.5px;line-height:16px}
.blog-more{position:absolute;left:18px;top:266px;font-size:10px;color:var(--orange)}

.quote-title{left:150px;top:1810px;width:505px;text-align:center;font-size:27px;line-height:31px}
.quote{left:175px;top:1890px;width:455px;text-align:center;font-size:11px;line-height:15.5px}
.quote-name{left:150px;top:1992px;width:505px;text-align:center;font-size:11px;font-weight:700;color:var(--ink)}
.quote-co{left:150px;top:2008px;width:505px;text-align:center;font-size:10px}
.arrow{width:30px;height:30px;border-radius:50%;display:flex;align-items:center;justify-content:center}

.close-title{left:606px;top:2843px;width:420px;font-size:25px;line-height:30px}
.close-copy{left:605px;top:2943px;width:430px;font-size:10.5px;line-height:15.5px}
.close-copy p{margin-bottom:15.5px}
.btn-dark{left:606px;top:3133px;width:120px;height:28px;background:var(--ink);color:var(--white);border-right:5px solid var(--orange)}

.footer{left:0;top:3255px;width:1200px;height:412px;background:var(--dark)}
.foot-head{font-size:14px;font-weight:600;color:var(--orange-soft)}
.foot-item{font-size:11px;color:var(--white);line-height:15px}
.foot-lbl{font-size:11px;color:var(--orange-soft)}
.foot-links{font-size:11px;color:var(--white);line-height:17.5px;list-style:none}
.map{left:769px;top:3438px;width:280px;height:153px;background:linear-gradient(135deg,#e9ece6,#d6dfd2)}
.copyright{left:150px;top:3640px;font-size:10px;color:var(--white);letter-spacing:.5px}
.foot-social{top:3636px;width:18px;height:18px;border-radius:50%}
</style>
</head>
<body>

<div class="abs hero"></div>
<div class="abs hero-photo" role="img" aria-label="Horse float with ramp lowered, hitched to a dark SUV on a green field under a cloudy sky"></div>
<div class="abs hero-shade"></div>
<div class="abs trailer-photo" role="img" aria-label="Twin axle horse float with front ramp down"></div>

<div class="abs call">Call</div>
<div class="abs phone">0400 555 018</div>
<div class="abs brand"><span class="brand-mark"></span><span class="brand-name">Marrowbeck Trailers</span></div>
<div class="abs socials">
  <span style="background:#3b5bb5"></span>
  <span style="background:#d8307a"></span>
  <span style="background:#1aa3e8"></span>
</div>
<nav class="abs nav" style="left:0;top:99px;width:1200px;height:20px">
  <a class="active" style="left:387px" href="#">Home</a>
  <a style="left:447px" href="#">Hire</a>
  <a style="left:491px" href="#">Trailers</a>
  <a style="left:554px" href="#">Horse Floats</a>
  <a style="left:646px" href="#">News</a>
  <a style="left:698px" href="#">Manuals</a>
  <a style="left:768px" href="#">Contact</a>
</nav>

<div class="abs hero-frame"></div>
<div class="abs hero-frame-line"></div>
<h1 class="abs hero-title">Built in Wales UK...<br>Engineered to the<br>highest standards...<br>Surviving the toughest<br>outback!</h1>
<div class="abs btn btn-sales">Sales</div>

<svg class="abs" style="left:0;top:556px" width="1200" height="34" viewBox="0 0 1200 34">
  <polygon fill="#d2462a" points="0,10 60,6 120,12 180,4 240,9 300,3 380,10 460,5 540,11 620,4 700,9 780,3 860,8 940,4 1020,10 1100,5 1200,8 1200,34 0,34"/>
  <polygon fill="#2a1b15" points="0,30 50,22 110,28 170,19 230,26 300,20 370,27 440,21 520,29 600,22 680,28 760,20 840,27 920,22 1000,28 1080,21 1150,27 1200,23 1200,34 0,34"/>
</svg>

<p class="abs covered">We have you covered for all of your<br>Tracka hire needs in Perth</p>
<div class="abs date" style="left:638px">
  <svg width="18" height="18" viewBox="0 0 18 18" fill="none" stroke="#d2462a" stroke-width="1.5"><rect x="2" y="3" width="14" height="13"/><line x1="2" y1="7" x2="16" y2="7"/><line x1="6" y1="1" x2="6" y2="5"/><line x1="12" y1="1" x2="12" y2="5"/></svg>
  <span class="lbl">Start Date</span><span class="val">DD/MM/YYYY</span>
</div>
<div class="abs date" style="left:777px">
  <svg width="18" height="18" viewBox="0 0 18 18" fill="none" stroke="#d2462a" stroke-width="1.5"><rect x="2" y="3" width="14" height="13"/><line x1="2" y1="7" x2="16" y2="7"/><line x1="6" y1="1" x2="6" y2="5"/><line x1="12" y1="1" x2="12" y2="5"/></svg>
  <span class="lbl">End Date</span><span class="val">DD/MM/YYYY</span>
</div>
<div class="abs date-go btn"><svg width="16" height="14" viewBox="0 0 16 14" fill="none" stroke="#fff" stroke-width="1.6"><rect x="1" y="3" width="7" height="8"/><path d="M8 7h6M11 4l3 3-3 3"/></svg></div>

<svg class="abs" style="left:0;top:728px" width="1200" height="36" viewBox="0 0 1200 36">
  <polygon fill="#d2462a" points="680,0 1200,0 1200,34"/>
</svg>

<div class="abs partner"><span class="partner-mark"></span><span class="partner-name">Dunmere Ashby<br>Trailers</span></div>
<h2 class="abs display intro-title">Quality Trailers +<br>Floats for Sale<br>in Perth</h2>
<p class="abs intro-sub">TRACKA, DIGMATE HIRE IN PERTH</p>
<div class="abs intro-copy">
  <p>Marrowbeck Trailers + Floats bring the Dunmere Ashby Trailers + Floats to the West Australian Market.</p>
  <p>Over 60 years in the business means that these trailers have stood the test of time.</p>
  <p>Used in areas from the remote north of Broome, on minesites, farms, hobby farms, and way down south, these trailers are doing it tough and exceeding expectations every time.</p>
</div>

<svg class="abs band" style="top:1080px" width="1200" height="625" viewBox="0 0 1200 625">
  <polygon fill="#0a0a0a" points="0,8 80,2 160,10 240,4 330,11 420,5 520,12 620,6 720,14 820,9 920,18 1020,14 1100,22 1200,20 1200,580 0,580"/>
  <polygon fill="#d2462a" points="0,578 400,578 1200,600 1200,620 0,600"/>
  <polygon fill="#0a0a0a" points="0,578 1200,578 1200,603 400,580 0,580"/>
</svg>
<h2 class="abs display section-title" style="top:1205px">Trailer Types</h2>

<div class="abs card" style="left:199px;top:1263px;height:303px">
  <div class="card-photo" role="img" aria-label="Silver twin axle horse float hitched to a car" style="background:linear-gradient(180deg,#c9cdd1,#8e9398)"></div>
  <div class="card-name">Horse Floats</div>
  <div class="card-code">QX408 / QX412</div>
</div>
<div class="abs card" style="left:474px;top:1263px;height:303px">
  <div class="card-photo" role="img" aria-label="Plant trailer loaded with an orange mini excavator" style="background:linear-gradient(180deg,#4f6f8f,#9aa0a3)"></div>
  <div class="card-name">Trailers</div>
  <div class="card-code">RV3072 / RV81</div>
</div>
<div class="abs card" style="left:749px;top:1263px;height:303px">
  <div class="card-photo" role="img" aria-label="Tipper trailer loaded with rocks at a quarry" style="background:linear-gradient(180deg,#b9b1a2,#7d7566)"></div>
  <div class="card-name">Tipper Trailers</div>
  <div class="card-code">LP5840 / 5296</div>
</div>

<h2 class="abs display quote-title">What Our<br>Customers Say</h2>
<p class="abs quote">To Callum and all the boys at Marrowbeck Trailers. Guys I can't thank you all enough for my brilliant 3.5tonne tipping trailer. I went to many places getting quotes and ideas for a multipurpose trailer that would do everything I needed in our landscaping business. Callum was the only one that truly listened to our requirements and had great input into the final design of the trailer.</p>
<p class="abs quote-name">Martin Aldercott</p>
<p class="abs quote-co">Aldercott Landscaping and Reticulation Service</p>
<div class="abs arrow" style="left:369px;top:2042px;border:1px solid #ddd"><svg width="10" height="10" viewBox="0 0 10 10" fill="none" stroke="#aaa" stroke-width="1.5"><path d="M7 1L3 5l4 4"/></svg></div>
<div class="abs arrow" style="left:405px;top:2042px;background:var(--orange)"><svg width="10" height="10" viewBox="0 0 10 10" fill="none" stroke="#fff" stroke-width="1.5"><path d="M3 1l4 4-4 4"/></svg></div>

<div class="abs" style="left:894px;top:1771px;width:165px;height:336px;background:var(--orange)"></div>
<div class="abs" style="left:699px;top:1781px;width:350px;height:316px;background:linear-gradient(180deg,#6e9ac8 0%,#a7b9c6 50%,#8a8d8c 100%)" role="img" aria-label="Orange skid steer loader on a galvanised plant trailer"></div>

<svg class="abs band" style="top:2128px" width="1200" height="625" viewBox="0 0 1200 625">
  <polygon fill="#0a0a0a" points="0,16 90,8 180,12 270,4 360,10 450,3 540,9 630,4 720,12 820,8 920,16 1020,12 1110,20 1200,18 1200,580 0,580"/>
  <polygon fill="#d2462a" points="0,580 1200,580 1200,595 0,600"/>
  <polygon fill="#0a0a0a" points="0,580 1200,580 1200,592 700,582"/>
</svg>
<h2 class="abs display section-title" style="top:2236px">Our Blog</h2>

<div class="abs card" style="left:199px;top:2295px;height:303px">
  <div class="blog-photo" role="img" aria-label="Green compact tracked loader with bucket in a workshop" style="background:linear-gradient(180deg,#b6b6b2,#5e7a3a)"></div>
  <div class="blog-date"><svg width="11" height="11" viewBox="0 0 11 11" fill="none" stroke="#d2462a" stroke-width="1.2"><rect x="1" y="2" width="9" height="8"/><line x1="1" y1="4.5" x2="10" y2="4.5"/></svg>19 Oct, 2023</div>
  <p class="blog-text">Lorem Ipsum is simply dummy text of the printing &amp; typesetting industry.</p>
  <span class="blog-more">Read More...</span>
</div>
<div class="abs card" style="left:474px;top:2295px;height:303px">
  <div class="blog-photo" role="img" aria-label="Yellow scissor lifts parked in a warehouse" style="background:linear-gradient(180deg,#d9a422,#6f6a5e)"></div>
  <div class="blog-date"><svg width="11" height="11" viewBox="0 0 11 11" fill="none" stroke="#d2462a" stroke-width="1.2"><rect x="1" y="2" width="9" height="8"/><line x1="1" y1="4.5" x2="10" y2="4.5"/></svg>19 Oct, 2023</div>
  <p class="blog-text">Lorem Ipsum is simply dummy text of the printing &amp; typesetting industry.</p>
  <span class="blog-more">Read More...</span>
</div>
<div class="abs card" style="left:749px;top:2295px;height:303px">
  <div class="blog-photo" role="img" aria-label="Caged trailer loaded with firewood" style="background:linear-gradient(180deg,#8a7a62,#a6a8a6)"></div>
  <div class="blog-date"><svg width="11" height="11" viewBox="0 0 11 11" fill="none" stroke="#d2462a" stroke-width="1.2"><rect x="1" y="2" width="9" height="8"/><line x1="1" y1="4.5" x2="10" y2="4.5"/></svg>19 Oct, 2023</div>
  <p class="blog-text">Lorem Ipsum is simply dummy text of the printing &amp; typesetting industry.</p>
  <span class="blog-more">Read More...</span>
</div>
<div class="abs btn" style="left:552px;top:2636px;width:96px;height:29px;background:var(--orange);color:var(--white);border-right:4px solid #fff;border-left:3px solid #fff">View All</div>

<div class="abs" style="left:149px;top:2807px;width:235px;height:385px;background:var(--orange)"></div>
<div class="abs" style="left:161px;top:2816px;width:373px;height:366px;background:linear-gradient(180deg,#5d7a45 0%,#9aa39a 45%,#6b8f3c 100%)" role="img" aria-label="Galvanised caged trailer with ramp carrying a ride-on mower and lawn mower on grass"></div>
<h2 class="abs display close-title">The Best Quality<br>Trailers Perth<br>has to Offer</h2>
<div class="abs close-copy">
  <p>We pride ourselves on supplying well designed and engineered trailers. Our team take the time to listen to our customers and supply trailers to suit their needs.</p>
  <p>We believe in the saying "Quality Counts". So we bring to bring to the West Australian market the Dunmere Ashby range of trailers.</p>
  <p>Whether you are looking for a trailer for commercial or domestic use. Dunmere Ashby Trailers are sure to offer a trailer that suits your needs.</p>
  <p>Dunmere Ashby Flatbed trailers, Tipper trailers and General Duty trailers are used across a huge variety of industries.</p>
</div>
<div class="abs btn btn-dark">Trailer Sales</div>

<div class="abs footer"></div>
<svg class="abs" style="left:0;top:3250px" width="1200" height="22" viewBox="0 0 1200 22">
  <polygon fill="#fff" points="0,0 1200,0 1200,10 1100,6 1000,12 900,5 800,11 700,4 600,10 500,5 400,12 300,6 200,11 100,4 0,9"/>
</svg>
<div class="abs brand" style="top:3338px"><span class="brand-mark"></span><span class="brand-name">Marrowbeck Trailers</span></div>

<div class="abs foot-head" style="left:152px;top:3443px">Contact Info</div>
<svg class="abs" style="left:152px;top:3472px" width="16" height="18" viewBox="0 0 16 18" fill="none" stroke="#d2462a" stroke-width="1.4"><path d="M8 17s6-6 6-10A6 6 0 0 0 2 7c0 4 6 10 6 10z"/><circle cx="8" cy="7" r="2"/></svg>
<div class="abs foot-lbl" style="left:176px;top:3470px">Address</div>
<div class="abs foot-item" style="left:176px;top:3484px">Unit 3, 88 Harlow Rd,<br>Brenton WA 6199</div>
<svg class="abs" style="left:152px;top:3524px" width="16" height="16" viewBox="0 0 16 16" fill="none" stroke="#d2462a" stroke-width="1.4"><path d="M3 1h3l1.5 4-2 1.5a9 9 0 0 0 4 4L11 8.5l4 1.5v3a2 2 0 0 1-2 2A13 13 0 0 1 1 3a2 2 0 0 1 2-2z"/></svg>
<div class="abs foot-lbl" style="left:176px;top:3520px">Call</div>
<div class="abs foot-item" style="left:176px;top:3535px">0400 555 018</div>
<svg class="abs" style="left:152px;top:3562px" width="16" height="13" viewBox="0 0 16 13" fill="none" stroke="#d2462a" stroke-width="1.4"><rect x="1" y="1" width="14" height="11"/><path d="M1 1l7 6 7-6"/></svg>
<div class="abs foot-lbl" style="left:176px;top:3557px">Email</div>
<div class="abs foot-item" style="left:176px;top:3572px">callum@marrowbecktrailers.com.au</div>

<div class="abs foot-head" style="left:423px;top:3440px">Information &amp; Products</div>
<ul class="abs foot-links" style="left:424px;top:3469px">
  <li>Contact us</li><li>Privacy Policy</li><li>Terms and Conditions</li><li>Operator Manuals</li><li>Machinery Specs</li><li>Videos</li><li>Terms &amp; Conditions</li>
</ul>
<ul class="abs foot-links" style="left:584px;top:3469px">
  <li>Hire</li><li>Car Trailers</li><li>Commercial Trailers</li><li>Box Van Trailers</li><li>Tipper Trailers</li><li>Horse Floats</li>
</ul>
<div class="abs map" role="img" aria-label="Street map showing the yard location"></div>

<div class="abs copyright">© 2023 Marrowbeck Trailers. All Right Reserved</div>
<span class="abs foot-social" style="left:926px;background:#3a2a24"></span>
<span class="abs foot-social" style="left:957px;top:3632px;width:26px;height:26px;background:var(--orange)"></span>
<span class="abs foot-social" style="left:990px;background:#3a2a24"></span>
<span class="abs foot-social" style="left:1022px;background:#3a2a24"></span>

</body>
</html>
```